Stationary and business card design for dental office
Dental Harbor
Simple
Merrow T. Pashley, DMD
Dental Harbor (use logo)
2870 W. Cobalt Mesa Rd. Ste #6
Las Vegas, NV 89047
pashleydmd@quarvix-mail.test
www.ourdentalharbor.test
Front of card to be gloss finish with the back to be a regular paper finish so that appointments can be written on the back.
My Next Appointment
Date:___________
Time:____________
Days of the week with boxes
Call Now
A simple map of the location to the right

```html
<!DOCTYPE html>
<html lang="en">
<head>
<meta charset="utf-8">
<title>Dental Harbor Stationery</title>
<link href="https://fonts.googleapis.com/css2?family=Libre+Baskerville:wght@400&family=Lato:wght@400;700&display=swap" rel="stylesheet">
<style>
  :root{
    --bg:#dcdadd;
    --paper:#ffffff;
    --brand:#2e7fa6;
    --teal:#2e9bbd;
    --sky:#bfe3f1;
    --ink:#3b3b3b;
    --rule:#9a9a9a;
    --shadow:rgba(0,0,0,.18);
  }
  *{box-sizing:border-box;margin:0;padding:0}
  html,body{width:1200px;height:538px;overflow:hidden;background:var(--bg)}
  body{position:relative;font-family:"Lato",sans-serif;color:var(--ink)}
  .sheet{position:absolute;background:var(--paper);box-shadow:1px 2px 5px var(--shadow);overflow:hidden}
  .wordmark{position:absolute;font-family:"Lato",sans-serif;font-weight:400;color:var(--brand);white-space:nowrap;letter-spacing:.5px}
  .watermark{position:absolute;border-radius:50%;background:radial-gradient(circle,rgba(46,155,189,.10),rgba(46,155,189,0) 70%)}
  .footer-line{position:absolute;left:0;right:0;text-align:center;font-family:"Libre Baskerville",serif;font-size:5.5px;line-height:8px;color:var(--teal);letter-spacing:.3px;white-space:nowrap}

  /* fax */
  .fax{left:12px;top:12px;width:384px;height:511px}
  .fax-title{position:absolute;left:30px;top:100px;font-size:26px;color:#222}
  .fax-fields{position:absolute;left:30px;top:148px;width:325px;display:grid;grid-template-columns:1fr 1fr;column-gap:14px;row-gap:9px}
  .field{display:flex;align-items:flex-end;gap:4px;font-size:5.5px;color:#555}
  .field span{flex:1;border-bottom:.8px solid var(--rule);height:7px}
  .comments{position:absolute;left:30px;top:246px;font-size:5.5px;color:#555}
  .checks{position:absolute;left:30px;top:265px;width:325px;display:flex;justify-content:space-between;font-size:5px;color:#555}
  .checks i{display:inline-block;width:6px;height:5px;border:.7px solid var(--rule);margin-right:3px;vertical-align:middle}

  /* letterhead */
  .letterhead{left:415px;top:19px;width:377px;height:504px}
  /* envelope */
  .envelope{left:809px;top:24px;width:381px;height:206px}
  .return{position:absolute;left:28px;top:154px;font-family:"Libre Baskerville",serif;font-size:5.5px;line-height:8px;color:#444}

  /* cards */
  .card{left:816px;width:173px;height:92px}
  .card-front{top:250px}
  .card-back{top:362px}
  .card-band{position:absolute;left:0;right:0;bottom:0;height:36px;background:linear-gradient(to bottom,#ffffff,var(--sky) 40%,var(--teal))}
  .card-name{position:absolute;left:10px;top:28px;font-family:"Libre Baskerville",serif;font-size:5px;color:#333}
  .card-contact{position:absolute;left:100px;top:10px;font-size:3.8px;line-height:5.5px;color:#444}
  .appt-title{position:absolute;left:10px;top:10px;font-family:"Libre Baskerville",serif;font-size:6px;color:#333}
  .appt-lines{position:absolute;left:10px;top:22px;width:150px;display:grid;row-gap:6px}
  .appt-lines .field{font-size:4.5px}
</style>
</head>
<body>

<!-- Fax sheet -->
<section class="sheet fax">
  <div class="watermark" style="left:20px;top:150px;width:340px;height:340px" role="img" aria-label="Large faint brand decoration"></div>
  <div class="wordmark" style="left:150px;top:28px;font-size:14px">Dental Harbor</div>
  <div class="fax-title">Fax</div>
  <div class="fax-fields">
    <div class="field">To:<span></span></div><div class="field">From:<span></span></div>
    <div class="field">Fax:<span></span></div><div class="field">Pages:<span></span></div>
    <div class="field">Phone:<span></span></div><div class="field">Date:<span></span></div>
    <div class="field">Re:<span></span></div><div class="field">CC:<span></span></div>
  </div>
  <div class="comments">Comments:</div>
  <div class="checks">
    <span><i></i>Urgent</span><span><i></i>For Review</span><span><i></i>Please Comment</span><span><i></i>Please Reply</span><span><i></i>Please Recycle</span>
  </div>
  <div class="footer-line" style="top:466px">2870 W. Cobalt Mesa Rd. Ste #6 · Las Vegas, NV 89047</div>
  <div class="footer-line" style="top:476px">P 702.555.0148 · F 702.555.0149</div>
  <div class="footer-line" style="top:486px">pashleydmd@quarvix-mail.test · www.ourdentalharbor.test</div>
</section>

<!-- Letterhead -->
<section class="sheet letterhead">
  <div class="watermark" style="left:20px;top:140px;width:340px;height:340px" role="img" aria-label="Large faint brand decoration"></div>
  <div class="wordmark" style="left:130px;top:36px;font-size:16px">Dental Harbor</div>
  <div class="footer-line" style="top:478px;font-size:5px">2870 W. Cobalt Mesa Rd. Ste #6 · Las Vegas, NV 89047 · 702.555.0148 · pashleydmd@quarvix-mail.test · www.ourdentalharbor.test</div>
</section>

<!-- Envelope -->
<section class="sheet envelope">
  <div class="watermark" style="left:-10px;top:-40px;width:180px;height:180px" role="img" aria-label="Faint brand decoration"></div>
  <div class="wordmark" style="left:262px;top:22px;font-size:12px">Dental Harbor</div>
  <div class="return">2870 W. Cobalt Mesa Rd. Ste #6<br>Las Vegas, NV 89047</div>
</section>

<!-- Business card front -->
<section class="sheet card card-front">
  <div class="wordmark" style="left:10px;top:10px;font-size:9px">Dental Harbor</div>
  <div class="card-name">Merrow T. Pashley, DMD</div>
  <div class="card-contact">2870 W. Cobalt Mesa Rd. Ste #6<br>Las Vegas, NV 89047<br>702.555.0148<br>pashleydmd@quarvix-mail.test<br>www.ourdentalharbor.test</div>
  <div class="card-band"></div>
</section>

<!-- Business card back -->
<section class="sheet card card-back">
  <div class="appt-title">My Next Appointment</div>
  <div class="appt-lines">
    <div class="field">Date:<span></span></div>
    <div class="field">Time:<span></span></div>
    <div class="field">Notes:<span></span></div>
  </div>
  <div class="card-band" style="height:28px"></div>
</section>

</body>
</html>
```